Laptop Accessories Packing Design

We are looking for a new package design of a laptop accesories (batteries, charges, hard drives etc.). We want to refresh our brand Velmora GridWorks. At VelmoraGrid, we create high-end laptop accessories that ensure reliability, performance, and longevity for users worldwide. Our mission is to deliver innovative and durable solutions that allow users to work, create, and grow without limits.
General Packaging Concept
Minimalist and elegant look, yet with elements that catch the eye (Velmora products will mainly be offered on auction portals such as Trivana, Zubo, Kestrix, so it would be good if the packaging attracted attention and stood out from the competitors).
Should I put a photo, sketch or product icon on the box? We'll leave that to your imagination.
We ask for a general design of the packaging. After the competition, together with the winner, we will add the rest of the information to the back and sides of the box.
In the attachments there is our Logo (you can use other colors) and sample packaging of competitors
Target Market(s)
E-commerse
Industry/Entity Type
individual end customer
Look and feel
Each slider illustrates characteristics of the customer's brand and the style your logo design should communicate.

```html
<!DOCTYPE html>
<html lang="en">
<head>
<meta charset="UTF-8">
<title>Velmora GridWorks – Packaging Front Panels</title>
<link href="https://fonts.googleapis.com/css2?family=Poppins:ital,wght@0,500;0,700;1,500&display=swap" rel="stylesheet">
<style>
  :root {
    --page-bg: #f5f5f5;
    --panel-black: #0b0b0b;
    --panel-grey: #3a3a3a;
    --gold-dark: #b9782a;
    --gold-mid: #d9a63a;
    --gold-light: #c9b866;
    --text-white: #f4f4f4;
  }
  * { margin: 0; padding: 0; box-sizing: border-box; }
  html, body {
    width: 867px; height: 1200px; overflow: hidden;
    background: var(--page-bg);
  }
  .canvas {
    position: relative; width: 867px; height: 1200px;
    display: flex; flex-direction: column; align-items: center;
    justify-content: space-around; padding: 90px 0;
  }
  .box-front {
    position: relative; width: 660px; height: 370px;
    display: flex; overflow: hidden;
    box-shadow: 0 18px 30px rgba(0,0,0,0.18);
  }
  .box-front__edge {
    flex: 0 0 50px;
    background: linear-gradient(90deg, var(--gold-dark), var(--gold-light) 45%, var(--gold-mid));
  }
  .box-front--striped .box-front__edge {
    flex: 0 0 50px;
    background:
      linear-gradient(90deg, var(--panel-black) 0 30%, transparent 30% 62%, var(--panel-black) 62%),
      linear-gradient(180deg, var(--gold-dark), var(--gold-light) 50%, var(--gold-dark));
  }
  .box-front__face {
    position: relative; flex: 1;
    background: radial-gradient(ellipse at 15% 0%, var(--panel-grey), var(--panel-black) 70%);
  }
  .box-front__pattern {
    position: absolute; inset: 0 40% 0 0;
    background: linear-gradient(90deg, rgba(217,166,58,0.28), rgba(217,166,58,0.08) 60%, rgba(217,166,58,0) 100%);
  }
  .brand {
    position: absolute; top: 22px; right: 28px;
    display: flex; flex-direction: column; align-items: flex-end;
    font-family: 'Poppins', sans-serif; font-weight: 700;
    color: var(--gold-mid);
  }
  .brand__name { font-size: 40px; line-height: 1; }
  .brand__sub {
    margin-top: 6px; font-size: 9px; letter-spacing: 5px;
    text-transform: uppercase;
  }
  .tagline {
    position: absolute; right: 18px; bottom: 50px;
    font-family: 'Poppins', sans-serif; font-style: italic; font-weight: 500;
    color: var(--text-white); font-size: 25px; letter-spacing: 3px;
    text-transform: uppercase; text-align: right; line-height: 1.25;
  }
</style>
</head>
<body>
<main class="canvas">
  <section class="box-front box-front--striped">
    <div class="box-front__edge"></div>
    <div class="box-front__face">
      <div class="box-front__pattern" role="img" aria-label="Gold honeycomb line pattern fading to the right"></div>
      <div class="brand">
        <span class="brand__name">Velmora</span>
        <span class="brand__sub">GridWorks</span>
      </div>
      <p class="tagline">High End<br>Laptop Accesories</p>
    </div>
  </section>

  <section class="box-front box-front--gold">
    <div class="box-front__edge"></div>
    <div class="box-front__face">
      <div class="box-front__pattern" role="img" aria-label="Gold honeycomb line pattern fading to the right"></div>
      <div class="brand">
        <span class="brand__name">Velmora</span>
        <span class="brand__sub">GridWorks</span>
      </div>
      <p class="tagline">High End<br>Laptop Accesories</p>
    </div>
  </section>
</main>
</body>
</html>
```